Upmarket Dessert Lounge needs a Business Card Design

We are an upmarket dessert lounge needing a business card to match our image.

We want something that is simple yet beautiful, feminine, classy, sophisticated and elegant. We want it to stand out and don't mind if it is bold.

The design should include our logo and colours of red or maroon with gold highlights. We don't mind if black is used.

Marlow & Quince

Target Market(s)

For those who like to indulge or treat themselves and give in to their temptations on good quality desserts.

Industry/Entity Type

Business

Requirements
Must have
• Must include our logo and our name

Marlow & Quince

M & Q

```html
<!DOCTYPE html>
<html lang="en">
<head>
<meta charset="utf-8">
<title>Marlow &amp; Quince — Business Card</title>
<link href="https://fonts.googleapis.com/css2?family=Cormorant+Garamond:wght@500;600&display=swap" rel="stylesheet">
<style>
  :root {
    --backdrop: #3b3b3d;
    --card-black: #161616;
    --card-black-edge: #1f1f1f;
    --maroon: #7b1416;
    --gold: #ecc98c;
    --card-w: 760px;
    --card-h: 434px;
  }
  * { margin: 0; padding: 0; box-sizing: border-box; }
  html, body {
    width: 1067px;
    height: 1200px;
    overflow: hidden;
    background: var(--backdrop);
    font-family: "Cormorant Garamond", Georgia, serif;
  }
  .sheet {
    position: relative;
    width: 1067px;
    height: 1200px;
  }
  .card {
    position: absolute;
    left: 153px;
    width: var(--card-w);
    height: var(--card-h);
    background: radial-gradient(ellipse at 40% 35%, var(--card-black-edge), var(--card-black) 70%);
    box-shadow: 0 14px 30px rgba(0,0,0,0.45);
    overflow: hidden;
    color: var(--gold);
  }
  .card--front { top: 120px; }
  .card--back { top: 646px; }

  /* Front */
  .front-band {
    position: absolute;
    left: 0; right: 0;
    top: 139px;
    height: 148px;
    background: var(--maroon);
    display: flex;
    align-items: center;
    justify-content: center;
  }
  .brand-name {
    font-weight: 500;
    letter-spacing: 0.04em;
    text-transform: uppercase;
    color: var(--gold);
    white-space: nowrap;
  }
  .front-band .brand-name { font-size: 50px; }
  .front-web {
    position: absolute;
    left: 0; right: 0;
    top: 350px;
    text-align: center;
    font-size: 26px;
    font-weight: 600;
    letter-spacing: 0.16em;
  }

  /* Back */
  .back-band {
    position: absolute;
    top: 0; bottom: 0;
    left: 72px;
    width: 236px;
    background: var(--maroon);
    display: flex;
    align-items: center;
    justify-content: center;
  }
  .back-band .brand-name {
    font-size: 27px;
    text-align: center;
    line-height: 1.15;
    white-space: normal;
  }
  .contact {
    position: absolute;
    left: 378px;
    top: 112px;
    font-weight: 600;
  }
  .contact-name {
    font-size: 25px;
    letter-spacing: 0.05em;
    text-transform: uppercase;
    font-weight: 500;
  }
  .contact-role {
    font-size: 16px;
    margin-bottom: 14px;
  }
  .contact-line {
    font-size: 17px;
    line-height: 1.4;
    letter-spacing: 0.03em;
  }
  .contact-web {
    margin-top: 8px;
    font-size: 21px;
    letter-spacing: 0.14em;
  }
</style>
</head>
<body>
<main class="sheet">
  <section class="card card--front" aria-label="Business card front">
    <div class="front-band">
      <span class="brand-name">Marlow &amp; Quince</span>
    </div>
    <p class="front-web">www.Marlow-Quince.com</p>
  </section>

  <section class="card card--back" aria-label="Business card back">
    <div class="back-band">
      <span class="brand-name">Marlow &amp;<br>Quince</span>
    </div>
    <div class="contact">
      <p class="contact-name">Maren Holt</p>
      <p class="contact-role">Manager</p>
      <p class="contact-line">m: + 123 555 0198 / f: + 123 555 0199</p>
      <p class="contact-line">e: mholt@marlow-quince.com</p>
      <p class="contact-web">www.marlow-quince.com</p>
    </div>
  </section>
</main>
</body>
</html>
```